Aircraft maintenance buisness card

I am an aircraft mechanic looking for a personal buisness card . I would like my name and a title of Aircraft Maintenance Manager . I would like a suttle picture of an aircraft and helicopter .

elegant and professional wtih my contact .

My name should be on the car and Aircraft Maintenance Manager under with my contact infor below .

i have attached some pictures but i am open to other pics and ideas . I would like a airliner or private jet and a helicopter in the picture . The Images should be suttle and not the main idea . I also uploaded a picture of a jet engine which is cool . Be creative and i will work with you to finalize something .
Updates

Project Deadline Extended
Reason: Looking for more variations . Very good so far but looiking for a bit more styles and i uploaded my logo that i purchased . Please use my logo and be creative with it . I like some variations of black card with maybe some pictures that i uploaded but i am open to ideas . Be creative and i will work with you .

Project Deadline Extended
Reason: Looking for more designs and variations . Not yet satisfied with the designs i have gotten .

Industry/Entity Type

Aviation

Contact Information for Business Card

Aircraft Maintenance Manager

Font styles to use
Serif

Colors

Designer to choose colors to be used in the design.

Requirements
Must have
• An aviation related Logo if possible incorporated in the card possibly
• My name
• Tiberio Malvade Furtunato
• 482 Pellow St.
• Halverd , KV
• 08519
• Email: Lwskyfixtech@mailvora.com
Nice to have
• Suttle Backround of a Private Jet or Airliner and a Helicopter .

```html
<!DOCTYPE html>
<html lang="en">
<head>
<meta charset="utf-8">
<title>Tiberio Malvade Furtunato – Business Card</title>
<link rel="stylesheet" href="https://fonts.googleapis.com/css2?family=Source+Sans+3:wght@400;600&display=swap">
<style>
  :root {
    --stage: #1b1b1b;
    --card-white: #ffffff;
    --orange: #f7941d;
    --orange-light: #f9a441;
    --ink: #3b3b3b;
    --text: #2a2a2a;
  }
  * { margin: 0; padding: 0; box-sizing: border-box; }
  html, body {
    width: 1200px; height: 900px; overflow: hidden;
    background: var(--stage);
    font-family: "Source Sans 3", sans-serif;
  }
  .stage { position: relative; width: 1200px; height: 900px; }
  .card {
    position: absolute; top: 306px;
    width: 440px; height: 271px;
    border-radius: 12px;
  }
  .card--front { left: 149px; background: var(--card-white); }
  .card--back {
    left: 608px;
    background: linear-gradient(180deg, var(--orange-light) 0%, var(--orange) 45%);
    display: flex; align-items: center; justify-content: center;
  }
  .brand {
    position: absolute; left: 30px; top: 116px; width: 165px;
    display: flex; align-items: center; gap: 8px;
    color: var(--ink); font-weight: 600; font-size: 30px; letter-spacing: 1px;
    white-space: nowrap;
  }
  .brand__dot {
    width: 14px; height: 14px; border-radius: 50%; background: var(--orange); flex: none;
  }
  .brand--large { position: static; width: auto; font-size: 62px; gap: 16px; }
  .brand--large .brand__dot { width: 26px; height: 26px; background: var(--ink); }
  .details { position: absolute; left: 209px; top: 70px; color: var(--text); white-space: nowrap; }
  .details__name { color: var(--orange); font-weight: 600; font-size: 15px; line-height: 18px; }
  .details__title { font-size: 12.5px; line-height: 16px; }
  .details__address { margin-top: 22px; font-size: 12.5px; line-height: 16px; }
  .details__contact { margin-top: 12px; font-size: 12.5px; line-height: 16px; }
  .contact-line { display: flex; align-items: center; gap: 6px; }
  .contact-line svg { width: 9px; height: 9px; fill: var(--orange); }
</style>
</head>
<body>
<main class="stage">
  <section class="card card--front">
    <div class="brand"><span class="brand__dot"></span>TMF Aero</div>
    <div class="details">
      <p class="details__name">Tiberio Malvade Furtunato</p>
      <p class="details__title">Aircraft Maintenance Manager</p>
      <p class="details__address">482 Pellow St.<br>Halverd , KV 08519</p>
      <div class="details__contact">
        <p class="contact-line">
          <svg viewBox="0 0 10 10" aria-hidden="true"><path d="M1 3c0-1 1-2 2-2h4c1 0 2 1 2 2v1H7V3H3v1H1zM2 5h6l1 4H1z"/></svg>
          222 555 817
        </p>
        <p class="contact-line">
          <svg viewBox="0 0 10 10" aria-hidden="true"><path d="M0 2h10v1L5 6 0 3zM0 4l5 3 5-3v4H0z"/></svg>
          Lwskyfixtech@mailvora.com
        </p>
      </div>
    </div>
  </section>
  <section class="card card--back">
    <div class="brand brand--large"><span class="brand__dot"></span>TMF Aero</div>
  </section>
</main>
</body>
</html>
```